Bref créative
BRFinishing Co.
NYC | Westchester |
Simple
Darrel Hutchins Jr
Project Manager
8 Lowell Terrace
Cold Meadow, NY 10488
brfinishinginfo@brfmail-example.com
We'd like to see ideas for vertical card designs as well.
It's all in the finish
Logo
logo

```html
<!DOCTYPE html>
<html lang="en">
<head>
<meta charset="utf-8">
<title>BRFinishing Co. — Business Card</title>
<link href="https://fonts.googleapis.com/css2?family=Open+Sans:wght@400&display=swap" rel="stylesheet">
<style>
  :root {
    --backdrop: #000000;
    --card: #e9e9e9;
    --slate: #3f4b53;
    --ink: #2b2b2b;
    --muted: #5a5a5a;
    --accent: #c9c9c9;
  }
  html, body {
    margin: 0;
    padding: 0;
    width: 1200px;
    height: 397px;
    overflow: hidden;
    background: var(--backdrop);
    font-family: "Open Sans", Arial, sans-serif;
  }
  .stage { position: relative; width: 1200px; height: 397px; }
  .card {
    position: absolute;
    top: 43px;
    width: 576px;
    height: 317px;
    background: var(--card);
    overflow: hidden;
  }
  .card--front { left: 12px; }
  .card--back { left: 612px; }
  .band { position: absolute; top: 0; left: 0; height: 100%; background: var(--slate); }
  .card--front .band { width: 41px; }
  .card--back .band { width: 180px; }
  .brand { position: absolute; display: flex; align-items: center; }
  .brand__square { background: var(--accent); flex: none; }
  .brand__name { font-weight: 400; color: var(--ink); white-space: nowrap; }
  .card--front .brand { left: 22px; top: 52px; }
  .card--front .brand__square { width: 38px; height: 38px; margin-right: 14px; }
  .card--front .brand__name { font-size: 30px; }
  .card--back .brand { left: 156px; top: 118px; }
  .card--back .brand__square { width: 48px; height: 48px; margin-right: 16px; }
  .card--back .brand__name { font-size: 36px; }
  .person { position: absolute; left: 53px; top: 160px; color: var(--muted); }
  .person__name { font-size: 22px; margin: 0; }
  .person__role { font-size: 12px; margin: 2px 0 0; }
  .contact {
    position: absolute; left: 286px; top: 202px;
    font-size: 12px; line-height: 19px; color: var(--muted);
    margin: 0; font-style: normal; white-space: nowrap;
  }
</style>
</head>
<body>
<div class="stage">
  <section class="card card--front">
    <div class="band"></div>
    <div class="brand">
      <span class="brand__square"></span>
      <span class="brand__name">BRFinishing Co.</span>
    </div>
    <div class="person">
      <p class="person__name">Darrel Hutchins Jr</p>
      <p class="person__role">Project Manager</p>
    </div>
    <address class="contact">
      8 Lowell Terrace<br>
      Cold Meadow, NY 10488<br>
      Phone: 347.555.0182<br>
      Email: brfinishinginfo@brfmail-example.com
    </address>
  </section>
  <section class="card card--back">
    <div class="band"></div>
    <div class="brand">
      <span class="brand__square"></span>
      <span class="brand__name">BRFinishing Co.</span>
    </div>
  </section>
</div>
</body>
</html>
```